diamondscoutline.com - Social Media Branding

diamondscoutline.com --> Social Media Re-Branding & Graphics
Facebook: @dmndscoutline - Instagram: @diamondscoutline - Twitter: @dmndscoutline

Looking to find a good designer to help with my diamondscoutline.com social media sites!
- facebook banner
- twitter banner
- instagram template (square and banner size)
- Quote or Information Template
- Committed Template (uniformed) - see the ones I made (& i am no professional) at diamondscoutline.com/committed - needs to have diamondscoutline.com logo, room for: the committed school and the team the player plays on.

Also willing to pay extra for a graphic that is the "complete package" that detail all of the steps of the recruiting process detailed in diamondscoutline.com

Font styles to use
Sans Serif

Colors
ec1f27
fbee3e

```html
<!DOCTYPE html>
<html lang="en">
<head>
<meta charset="utf-8">
<title>diamondscoutline.com – Social Media Kit</title>
<link href="https://fonts.googleapis.com/css2?family=Barlow:wght@400;500;600;700;800&display=swap" rel="stylesheet">
<style>
:root{
  --red:#ec1f27;
  --deep-red:#c21d2c;
  --yellow:#fbee3e;
  --soft-yellow:#f6f19a;
  --ink:#111111;
  --paper:#ffffff;
  --cover-bg:#f5f3f4;
  --fb-blue:#3b5998;
  --tw-blue:#1da1f2;
  --line:#dddfe2;
  --grey:#8a8d91;
}
*{box-sizing:border-box;margin:0;padding:0}
html,body{width:1143px;height:1200px;overflow:hidden;background:var(--paper)}
body{position:relative;font-family:"Barlow",sans-serif;color:var(--ink)}
.panel{position:absolute;background:var(--paper);box-shadow:0 8px 18px rgba(0,0,0,.28);overflow:hidden}
.cover-art{position:absolute;left:0;top:0;display:block}
.wordmark{font-family:"Barlow",sans-serif;font-weight:800;color:var(--ink);white-space:nowrap;letter-spacing:.2px}

/* twitter header */
.twitter{left:122px;top:68px;width:898px;height:396px}
.twitter .brand{position:absolute;left:540px;top:90px;width:320px;text-align:center}
.twitter .brand .wordmark{font-size:34px}
.handles{position:absolute;display:flex;justify-content:space-between}
.twitter .handles{left:490px;top:208px;width:400px}
.handle{display:flex;flex-direction:column;align-items:center;gap:6px;font-weight:500}
.twitter .handle{font-size:15px}
.handle .dot{width:22px;height:22px;border-radius:50%;border:2px solid var(--red)}
.avatar{position:absolute;border-radius:50%;background:var(--paper);border:2px solid #e6e6e6;display:flex;align-items:center;justify-content:center;text-align:center}
.avatar .wordmark{font-size:18px;line-height:1.1}
.twitter .avatar{left:152px;top:254px;width:196px;height:196px}
.follow-btn{position:absolute;left:755px;top:311px;width:116px;height:56px;border:2px solid var(--tw-blue);border-radius:28px;color:var(--tw-blue);font-weight:700;font-size:22px;display:flex;align-items:center;justify-content:center}

/* facebook page */
.facebook{left:122px;top:503px;width:898px;height:260px}
.facebook .brand{position:absolute;left:548px;top:74px;width:240px;text-align:center}
.facebook .brand .wordmark{font-size:21px}
.facebook .handles{left:512px;top:120px;width:250px}
.facebook .handle{font-size:8px;gap:3px;color:#444}
.facebook .handle .dot{width:12px;height:12px;border-width:1.5px}
.facebook .avatar{left:20px;top:68px;width:174px;height:174px;border-width:3px}
.facebook .avatar .wordmark{font-size:16px}
.action{position:absolute;top:173px;height:26px;background:var(--paper);border:1px solid var(--line);font-weight:600;font-size:13px;color:#4b4f56;display:flex;align-items:center;justify-content:center;gap:5px}
.action.update{left:597px;width:110px}
.badge{background:var(--red);color:#fff;font-size:10px;padding:0 3px;border-radius:2px;line-height:14px}
.action.log{left:729px;width:115px}
.action.more-dots{left:844px;width:36px;letter-spacing:1px}
.tabs{position:absolute;left:0;top:217px;width:898px;height:43px;background:var(--paper);display:flex;padding-left:213px}
.tab{height:100%;border-left:1px solid var(--line);display:flex;align-items:center;justify-content:center;gap:5px;color:var(--fb-blue);font-weight:600;font-size:15px}
.tab:last-child{border-right:1px solid var(--line)}
.tab .count{color:var(--grey);font-weight:400;font-size:12px}
.caret{width:0;height:0;border-left:4px solid transparent;border-right:4px solid transparent;border-top:5px solid var(--fb-blue)}

/* squares */
.square{top:810px;width:322px;height:321px}
.action-post{left:41px}
.quote-post{left:411px}
.committed-post{left:780px}
.photo{position:absolute}
.action-post .wordmark{position:absolute;right:12px;bottom:14px;font-size:11.5px}
.quote-post .pattern{position:absolute;inset:0}
.quote-post .wordmark{position:absolute;left:20px;top:14px;font-size:11.5px}
.quote-bubble{position:absolute;left:58px;top:68px;width:200px;height:200px;border-radius:50%;background:var(--deep-red);box-shadow:0 6px 14px rgba(0,0,0,.3);color:#fff;text-align:center;padding:18px 20px 0}
.quote-mark{font-size:64px;font-weight:800;color:var(--yellow);line-height:54px;height:44px;font-style:normal}
.quote-text{font-size:12px;line-height:16px;margin-top:8px}
.quote-author{font-size:10.5px;margin-top:12px;font-weight:500}
.school{position:absolute;left:12px;top:10px;display:flex;align-items:center;gap:6px}
.school .seal{width:16px;height:16px;border-radius:50%;border:1px solid var(--red)}
.school-name{font-size:13px;font-weight:500;line-height:1}
.school-name small{display:block;font-size:5.5px;letter-spacing:2.6px;margin-top:2px}
.team{position:absolute;right:14px;top:10px;font-size:21px;font-weight:800;color:#e05a1e}
.congrats{position:absolute;left:130px;top:150px;width:220px;transform:rotate(-45deg);transform-origin:left top;text-align:center}
.committed-post .banner-text{position:absolute;left:118px;top:268px;transform:rotate(-45deg);transform-origin:left bottom;white-space:nowrap}
.banner-text .headline{font-size:24px;font-weight:800;color:var(--red);letter-spacing:.5px;line-height:1}
.banner-text .player{font-size:18px;font-weight:500;margin-left:52px;line-height:1}
.committed-post .ball{position:absolute;right:24px;bottom:14px;width:44px;height:44px;border-radius:50%;background:var(--yellow)}
.committed-post .wordmark{position:absolute;left:14px;bottom:14px;font-size:11.5px}
</style>
</head>
<body>

<!-- Twitter header -->
<section class="panel twitter">
  <svg class="cover-art" width="898" height="299" viewBox="0 0 898 299">
    <defs><linearGradient id="twShade" x1="0" y1="0" x2="1" y2="1"><stop offset="0" stop-color="#6d6d6d"/><stop offset=".6" stop-color="#9a9a9a"/><stop offset="1" stop-color="#505050"/></linearGradient></defs>
    <rect width="898" height="299" fill="var(--cover-bg)"/>
    <path d="M0,0 L432,0 Q640,150 340,299 L0,299 Z" fill="url(#twShade)" role="img" aria-label="Photo of a catcher in red gear holding her helmet, softball in the dirt"/>
    <path d="M432,0 Q640,150 340,299" fill="none" stroke="var(--red)" stroke-width="8"/>
  </svg>
  <div class="brand"><span class="wordmark">diamondscoutline.com</span></div>
  <div class="handles">
    <div class="handle"><span class="dot"></span>@dmndscoutline</div>
    <div class="handle"><span class="dot"></span>@diamondscoutline</div>
    <div class="handle"><span class="dot"></span>@dmndscoutline</div>
  </div>
  <div class="avatar"><span class="wordmark">diamond<br>scoutline</span></div>
  <div class="follow-btn">Follow</div>
</section>

<!-- Facebook page -->
<section class="panel facebook">
  <svg class="cover-art" width="898" height="217" viewBox="0 0 898 217">
    <defs><linearGradient id="fbShade" x1="0" y1="0" x2="1" y2="1"><stop offset="0" stop-color="#6d6d6d"/><stop offset=".6" stop-color="#9a9a9a"/><stop offset="1" stop-color="#505050"/></linearGradient></defs>
    <rect width="898" height="217" fill="var(--cover-bg)"/>
    <path d="M0,0 L419,0 Q557,110 352,217 L0,217 Z" fill="url(#fbShade)" role="img" aria-label="Photo of a catcher in red gear holding her helmet, softball in the dirt"/>
    <path d="M419,0 Q557,110 352,217" fill="none" stroke="var(--red)" stroke-width="7"/>
  </svg>
  <div class="brand"><span class="wordmark">diamondscoutline.com</span></div>
  <div class="handles">
    <div class="handle"><span class="dot"></span>@dmndscoutline</div>
    <div class="handle"><span class="dot"></span>@diamondscoutline</div>
    <div class="handle"><span class="dot"></span>@dmndscoutline</div>
  </div>
  <div class="action update">Update Info <span class="badge">3</span></div>
  <div class="action log">
    <svg width="14" height="12" viewBox="0 0 14 12"><g fill="#4b4f56"><rect x="0" y="1" width="2" height="2"/><rect x="0" y="5" width="2" height="2"/><rect x="0" y="9" width="2" height="2"/><rect x="4" y="1.5" width="10" height="1"/><rect x="4" y="5.5" width="10" height="1"/><rect x="4" y="9.5" width="10" height="1"/></g></svg>
    Activity Log</div>
  <div class="action more-dots">···</div>
  <nav class="tabs">
    <div class="tab" style="width:113px">Timeline <span class="caret"></span></div>
    <div class="tab" style="width:79px">About</div>
    <div class="tab" style="width:110px">Friends <span class="count">14</span></div>
    <div class="tab" style="width:86px">Photos</div>
    <div class="tab" style="width:112px">
      <svg width="11" height="13" viewBox="0 0 11 13"><path d="M2.5,6 V4 a3,3 0 0 1 6,0 V6" fill="none" stroke="var(--fb-blue)" stroke-width="1.8"/><rect x="0.5" y="6" width="10" height="7" rx="1" fill="var(--fb-blue)"/></svg>
      Archive</div>
    <div class="tab" style="width:90px">More <span class="caret"></span></div>
  </nav>
  <div class="avatar"><span class="wordmark">diamond<br>scoutline</span></div>
</section>

<!-- Action photo post -->
<section class="panel square action-post">
  <svg class="photo" width="322" height="321" viewBox="0 0 322 321">
    <defs><linearGradient id="playShade" x1="0" y1="0" x2="0" y2="1"><stop offset="0" stop-color="#6f8a5c"/><stop offset=".45" stop-color="#c9b36a"/><stop offset="1" stop-color="#e3c9a6"/></linearGradient></defs>
    <rect width="322" height="321" fill="url(#playShade)" role="img" aria-label="Photo of a runner sliding into home plate as the catcher reaches for the tag"/>
    <path d="M322,200 Q250,230 170,321 L322,321 Z" fill="var(--paper)"/>
    <path d="M322,200 Q250,230 170,321" fill="none" stroke="var(--red)" stroke-width="5"/>
  </svg>
  <span class="wordmark">diamondscoutline.com</span>
</section>

<!-- Quote post -->
<section class="panel square quote-post">
  <div class="pattern" role="img" aria-label="Scattered softball pattern" style="background:radial-gradient(circle at 30% 20%,#fbf6c4 0,transparent 40%),radial-gradient(circle at 80% 80%,#fbf6c4 0,transparent 40%),var(--paper)"></div>
  <span class="wordmark">diamondscoutline.com</span>
  <div class="quote-bubble">
    <div class="quote-mark">“</div>
    <p class="quote-text">If you want something you’ve never had, you must be willing to do something you’ve never done.</p>
    <p class="quote-author">- HAROLD WHITFIELD</p>
  </div>
</section>

<!-- Committed post -->
<section class="panel square committed-post">
  <svg class="photo" width="322" height="321" viewBox="0 0 322 321">
    <defs>
      <linearGradient id="pitchShade" x1="0" y1="0" x2="1" y2="1"><stop offset="0" stop-color="#3c3a2a"/><stop offset=".5" stop-color="#8a6d3e"/><stop offset="1" stop-color="#c9955a"/></linearGradient>
      <clipPath id="cutCircle"><path d="M0,0 H290 L110,321 H0 Z"/></clipPath>
    </defs>
    <circle cx="162" cy="155" r="134" fill="url(#pitchShade)" clip-path="url(#cutCircle)" role="img" aria-label="Photo of a pitcher in a red uniform winding up at sunset"/>
  </svg>
  <div class="school"><span class="seal"></span><span class="school-name">Lakeridge<small>UNIVERSITY</small></span></div>
  <div class="team">Comets</div>
  <div class="banner-text">
    <div class="headline">CONGRATULATIONS</div>
    <div class="player">Jenna Marlowe</div>
  </div>
  <span class="ball"></span>
  <span class="wordmark">diamondscoutline.com</span>
</section>

</body>
</html>
```